One page website

I'm looking for a landing page for my company. Just a brief description of our medical device technology with some images

Coding

Coded - Design and coding required

```html
<!DOCTYPE html>
<html lang="en">
<head>
<meta charset="utf-8">
<title>Veltra Surgical – Landing Page Layouts</title>
<link rel="stylesheet" href="https://fonts.googleapis.com/css2?family=Arimo:wght@400;700&display=swap">
<style>
:root{
  --green:#97bb55;
  --green-deep:#8fb44c;
  --blue:#3aa2da;
  --blue-light:#a9d8ef;
  --ink:#1c1c1c;
  --body:#333;
  --muted:#666;
  --red:#e3232b;
  --teal:#24606d;
  --white:#fff;
  --xray-dark:#0b0f10;
  --xray-light:#9fd6cf;
}
*{box-sizing:border-box;margin:0;padding:0}
html,body{width:1200px;height:1200px;overflow:hidden;background:var(--white)}
body{font-family:"Arimo",Arial,sans-serif;color:var(--ink)}
.board{position:relative;width:1500px;height:1500px;transform:scale(.8);transform-origin:0 0}
.abs{position:absolute}
.page{position:absolute;top:0;width:401px;height:1490px;overflow:hidden;background:var(--white)}
.page--menu-closed{left:131px}
.page--menu-open{left:554px}
.section{position:absolute;left:0;width:100%}
.brand{font-size:10px;color:var(--green);font-weight:400;line-height:1}
.hero-title{font-size:24px;font-weight:700;line-height:1}
.hero-sub{font-size:20px;line-height:1}
.h-white{color:var(--white);font-weight:700;font-size:14px}
.h-blue{color:var(--blue);font-weight:700;font-size:14px}
.h-small-blue{color:var(--blue);font-weight:700;font-size:11px}
.h-center{text-align:center;width:100%}
.copy{font-size:9.5px;line-height:1.3;color:var(--body)}
.small{font-size:6.5px;line-height:1.3;color:var(--body)}
.tiny{font-size:5px;line-height:1.3;color:var(--body)}
.tiny-white{font-size:5px;line-height:1.3;color:var(--white)}
.small-white{font-size:6.5px;line-height:1.3;color:var(--white)}
.bold{font-weight:700}
.ital{font-style:italic}
.caption-blue{font-size:8.5px;color:var(--blue)}
.link-red{color:var(--red);text-decoration:underline}
.photo{position:absolute}
.xray{background:radial-gradient(ellipse at 50% 50%,var(--xray-light) 0%,#4d7d78 35%,var(--xray-dark) 80%)}
.xray-grey{background:radial-gradient(ellipse at 50% 50%,#d0d0d0 0%,#8a8a8a 45%,#3a3a3a 100%)}
.brace-photo{border-radius:50%;background:radial-gradient(circle at 55% 50%,#efe6df 0%,#c8ada0 45%,#3a5870 85%)}
.spine-photo{background:linear-gradient(90deg,#d9cdb8,#f3ece0 50%,#c4b59c)}
.icon-dot{position:absolute;width:26px;height:26px;border-radius:50%;background:var(--blue);border:2px solid var(--white);margin:-13px 0 0 -13px}
.result-dot{position:absolute;width:30px;height:30px;border-radius:50%;background:var(--blue);margin:-15px 0 0 -15px}
.menu-panel{position:absolute;background:rgba(175,205,120,.82)}
.menu-panel li{list-style:none;font-size:5px;line-height:8.5px;color:#2a2a2a;text-transform:uppercase}
.menu-panel li.is-active{background:rgba(120,160,60,.9);color:var(--white)}
.col-right{position:absolute;left:978px;top:0;width:386px;height:1500px;overflow:hidden;background:var(--white)}
.card{position:absolute;background:var(--white)}
.market-col{position:absolute;top:0;width:106px;height:139px}
.market-col ul{position:absolute;top:74px;left:12px;width:90px}
.market-col li,.timeline li,.team-role{font-size:5px;line-height:1.3;color:var(--muted)}
.market-col li{list-style:none}
.market-col li::before{content:"• "}
.coin{position:absolute;width:30px;height:30px;border-radius:50%;background:#7cbb2a;color:var(--white);font-size:5px;text-align:center;line-height:30px;font-weight:700}
.timeline{position:absolute;left:1013px;top:766px;width:319px;height:136px;background:linear-gradient(180deg,#2d6470 0%,#3e7482 22%,#dfe6e7 22%,#eef2f3 100%)}
.tl-col{position:absolute;top:0;width:44px}
.tl-head{font-size:6px;color:var(--white);font-weight:700;text-align:center;margin-top:30px}
.tl-tick{width:11px;height:11px;border-radius:50%;background:#6cb33f;margin:13px auto 6px}
.timeline li{list-style:none;color:#2c5a8a;font-size:4.8px}
.timeline li::before{content:"• "}
.bullets li{font-size:7.5px;line-height:13px;color:var(--body);list-style:none;padding-left:12px;position:relative}
.bullets li::before{content:"";position:absolute;left:2px;top:4px;width:4px;height:4px;border-radius:50%;background:var(--ink)}
.kp-row{position:absolute;left:152px;font-size:5.5px;font-weight:700;line-height:1.3;color:var(--ink)}
.kp-icon{position:absolute;left:-24px;top:-3px;width:16px;height:16px;border-radius:50%;background:#9aa3a6}
.member{position:absolute;width:110px}
.member-photo{position:absolute;left:0;top:0;width:20px;height:22px;background:linear-gradient(180deg,#b9a89a,#6f5f55)}
.member-name{position:absolute;left:26px;top:0;font-size:6.5px;font-weight:700;color:var(--ink)}
.team-role{position:absolute;left:26px;top:8px;width:82px;font-size:4.2px}
.note{position:absolute;color:var(--red);font-size:16px;line-height:1.35}
</style>
</head>
<body>
<main class="board">

<!-- ============ PAGE: MENU CLOSED ============ -->
<section class="page page--menu-closed">
  <svg class="abs" style="left:0;top:0" width="401" height="200" role="img" aria-label="Child stretching on a white floor inside a round frame">
    <circle cx="310" cy="50" r="118" fill="#e9eef3"/>
    <path d="M190 94 A128 128 0 0 0 374 161" fill="none" stroke="var(--blue)" stroke-width="8"/>
    <path d="M170 62 A140 140 0 0 0 409 149" fill="none" stroke="var(--green)" stroke-width="13"/>
  </svg>
  <div class="abs brand" style="left:35px;top:40px">Veltra Surgical</div>
  <svg class="abs" style="left:35px;top:72px" width="12" height="10"><path d="M0 1H12M0 5H12M0 9H12" stroke="var(--green)" stroke-width="1.4"/></svg>
  <div class="abs hero-title" style="left:35px;top:139px">Solving</div>
  <div class="abs hero-sub" style="left:35px;top:166px">Children’s Scoliosis</div>

  <div class="section" style="top:200px;height:130px;background:var(--green);border-bottom-left-radius:70% 16px">
    <div class="abs h-white" style="left:35px;top:27px">MISSION</div>
    <p class="abs copy" style="left:65px;top:60px;width:290px">Develop novel technologies focusing on non-fusion scoliosis correctionallowing for non-surgical dynamic adustment of implants over time.</p>
  </div>

  <div class="abs h-blue" style="left:37px;top:354px">PROBLEM</div>
  <p class="abs copy" style="left:37px;top:377px;width:330px">Scoliosis affects 2-3% of the population, or an estimated <b>6-9 million people</b> in the U.S.</p>
  <div class="photo xray" style="left:49px;top:422px;width:85px;height:75px" role="img" aria-label="X-ray of a mild scoliosis spine"></div>
  <div class="photo xray" style="left:161px;top:422px;width:85px;height:75px" role="img" aria-label="X-ray of a moderate scoliosis spine"></div>
  <div class="photo xray" style="left:275px;top:422px;width:85px;height:75px" role="img" aria-label="X-ray of a severe scoliosis spine"></div>
  <div class="abs caption-blue" style="left:49px;top:505px">Mild Scoliosis</div>
  <div class="abs caption-blue" style="left:161px;top:505px">Moderate Scoliosis</div>
  <div class="abs caption-blue" style="left:275px;top:505px">Severe Scoliosis</div>
  <div class="abs tiny" style="left:49px;top:521px">10- to 24-degree Cobb<br>Treatment: Monitoring</div>
  <div class="abs tiny" style="left:161px;top:521px">25- to 39-degree Cobb<br>Treatment: <span class="link-red">Bracing</span></div>
  <div class="abs tiny" style="left:275px;top:521px">+40- to 50-degree Cobb<br>Treatment: <span class="link-red">Fusion</span></div>

  <svg class="abs" style="left:0;top:538px" width="401" height="430"><path d="M0 4 C60 -4 110 22 170 24 L401 24 L401 430 L0 430 Z" fill="var(--blue-light)"/></svg>
  <div class="abs h-blue" style="left:37px;top:589px">SOLUTIONS</div>
  <div class="photo brace-photo" style="left:50px;top:625px;width:134px;height:134px" role="img" aria-label="Child wearing a white scoliosis brace"></div>
  <div class="abs h-small-blue" style="left:206px;top:628px">BRACING</div>
  <div class="abs small" style="left:206px;top:653px">For scoliosis patients with Cobb 25-39°<br>Start bracing as early as 2 years old</div>
  <div class="abs small" style="left:206px;top:679px"><span class="bold" style="font-size:8px">Bracing Limitations</span><br>Poor Compliance (50%)<br>Rarely straighten spine<br>Multi-year treatment</div>
  <div class="abs h-small-blue" style="left:47px;top:796px">FUSION</div>
  <div class="photo xray-grey" style="left:212px;top:798px;width:145px;height:90px;border:3px solid #111" role="img" aria-label="Front and side X-rays of a fused spine with rods"></div>
  <div class="abs small" style="left:47px;top:820px;width:160px">For scoliosis patients with Cobb &gt; 40-50°<br>Fusion on early onset scoliosis and adolescent idiopathic scoliosis (AIS) patients</div>
  <div class="abs small" style="left:47px;top:853px;width:160px"><span class="bold" style="font-size:8px">Fusion Limitations</span><br>4+ hour surgery<br>Fusion is irreversible<br>Complications, infections, failures<br>Limiting motion for life<br>Adjacent segment disease: <i>illnesses caused around a fusion site. Most commonly occurs due to physical stress on surrounding spinal segments after a fusion operation</i></div>

  <div class="section" style="top:965px;height:220px;background:var(--blue)">
    <div class="abs h-white" style="left:47px;top:22px;font-size:11px;line-height:1.3">NON-FUSION<br>Vertebral Body Tethering (VBT)</div>
    <div class="photo spine-photo" style="left:47px;top:62px;width:62px;height:135px" role="img" aria-label="Spine model with vertebral body tether"></div>
    <div class="abs small-white" style="left:150px;top:65px;width:205px">Cobb &gt; 40°<br>For early onset scoliosis patients with skeletal growth remaining<br>Ages generally 8-12<br>Procedure currently performed by 15-20 surgeons</div>
    <div class="abs small-white" style="left:150px;top:106px;width:210px"><span class="bold" style="font-size:8px">Limitations</span><br>No ability to adjust tether. Over-correction can result.<br>Tethers break – 10% breakage rate per data submitted to FDA</div>
    <div class="abs small-white ital" style="left:150px;top:141px;width:210px">Halden System recently approved by FDA under HDE Exemption.<br>Provides regulatory clarity</div>
  </div>

  <div class="section" style="top:1185px;height:150px;background:var(--green)">
    <div class="photo" style="left:85px;top:28px;width:260px;height:102px;background:linear-gradient(90deg,rgba(255,255,255,.05),rgba(255,255,255,.18),rgba(255,255,255,.05))" role="img" aria-label="Faint photo of active children behind the icons"></div>
    <div class="abs h-center bold" style="top:17px;font-size:11px">Advantages of VBT over Fusion</div>
    <div class="abs tiny-white" style="left:84px;top:44px;width:30px;text-align:center;color:#2a3a18">Continued skeletal growth</div>
    <div class="abs tiny-white" style="left:178px;top:48px;width:40px;text-align:center;color:#2a3a18">Single treatment event</div>
    <div class="abs tiny" style="left:268px;top:44px;width:70px;text-align:center;color:#2a3a18"><b>Does not “burn any bridge”</b><br>Future revision and fusion remain possible</div>
    <div class="icon-dot" style="left:98px;top:81px"></div>
    <div class="icon-dot" style="left:148px;top:81px"></div>
    <div class="icon-dot" style="left:201px;top:81px"></div>
    <div class="icon-dot" style="left:249px;top:81px"></div>
    <div class="icon-dot" style="left:301px;top:81px"></div>
    <div class="abs tiny" style="left:131px;top:102px;width:34px;text-align:center;color:#2a3a18">Partial Motion Preservation</div>
    <div class="abs tiny" style="left:226px;top:102px;width:46px;text-align:center;color:#2a3a18">Little impact on activity and appearance</div>
  </div>

  <div class="abs h-small-blue h-center" style="top:1355px">VBT has Proven Results</div>
  <p class="abs copy" style="left:55px;top:1376px;width:291px;text-align:center;font-size:8.5px">Between the Northbridge group and Dr. Morrow at Bayview University Medical Center (BUMC), 350+ VBT procedures were completed.</p>
  <div class="result-dot" style="left:76px;top:1429px"></div>
  <div class="result-dot" style="left:160px;top:1429px"></div>
  <div class="result-dot" style="left:245px;top:1429px"></div>
  <div class="result-dot" style="left:330px;top:1429px"></div>
  <div class="abs tiny" style="left:41px;top:1455px;width:70px;text-align:center">~66% Cost Savings ($50K compared to $150K)</div>
  <div class="abs tiny" style="left:125px;top:1455px;width:70px;text-align:center">50% Saving in Surgery Time (1.5-2 hrs compared to 4-8 hrs)</div>
  <div class="abs tiny" style="left:210px;top:1455px;width:70px;text-align:center">50% Saving in Hospital Stay (2-3 days compared to 6-7 days)</div>
  <div class="abs tiny" style="left:295px;top:1455px;width:70px;text-align:center">Confirmed improved self-confidence for surgical recipients</div>
</section>

<!-- ============ PAGE: MENU OPEN ============ -->
<section class="page page--menu-open">
  <svg class="abs" style="left:0;top:0" width="401" height="200" role="img" aria-label="Child stretching on a white floor inside a round frame">
    <circle cx="310" cy="50" r="118" fill="#e9eef3"/>
    <path d="M190 94 A128 128 0 0 0 374 161" fill="none" stroke="var(--blue)" stroke-width="8"/>
    <path d="M170 62 A140 140 0 0 0 409 149" fill="none" stroke="var(--green)" stroke-width="13"/>
  </svg>
  <div class="abs brand" style="left:35px;top:40px">Veltra Surgical</div>
  <div class="abs hero-title" style="left:35px;top:139px">Solving</div>
  <div class="abs hero-sub" style="left:35px;top:166px">Children’s Scoliosis</div>
  <ul class="menu-panel" style="left:0;top:85px;width:138px;height:105px;padding:1px 0">
    <li class="is-active" style="padding-left:35px">Mission</li>
    <li style="padding-left:35px">The Problems</li>
    <li style="padding-left:35px">Solutions</li>
    <li style="padding-left:35px">Vertebral Body Tethering (VBT)</li>
    <li style="padding-left:35px">Advantages of VBT</li>
    <li style="padding-left:35px">Magnetic Tensioning</li>
    <li style="padding-left:35px">Pilot Pig Study</li>
    <li style="padding-left:35px">Tethering Marketing Segments</li>
    <li style="padding-left:35px">Timeline</li>
    <li style="padding-left:35px">Accomplishment</li>
    <li style="padding-left:35px">Key Points for Investment</li>
    <li style="padding-left:35px">Founding Team</li>
  </ul>
  <svg class="abs" style="left:37px;top:72px" width="9" height="9"><path d="M0 0L9 9M9 0L0 9" stroke="var(--green)" stroke-width="1.3"/></svg>

  <div class="section" style="top:200px;height:130px;background:var(--green);border-bottom-left-radius:70% 16px">
    <div class="abs h-white" style="left:35px;top:27px">MISSION</div>
    <p class="abs copy" style="left:65px;top:60px;width:290px">Develop novel technologies focusing on non-fusion scoliosis correctionallowing for non-surgical dynamic adustment of implants over time.</p>
  </div>

  <div class="abs h-blue" style="left:37px;top:354px">PROBLEM</div>
  <p class="abs copy" style="left:37px;top:377px;width:330px">Scoliosis affects 2-3% of the population, or an estimated <b>6-9 million people</b> in the U.S.</p>
  <div class="photo xray" style="left:49px;top:422px;width:85px;height:75px" role="img" aria-label="X-ray of a mild scoliosis spine"></div>
  <div class="photo xray" style="left:161px;top:422px;width:85px;height:75px" role="img" aria-label="X-ray of a moderate scoliosis spine"></div>
  <div class="photo xray" style="left:275px;top:422px;width:85px;height:75px" role="img" aria-label="X-ray of a severe scoliosis spine"></div>
  <div class="abs caption-blue" style="left:49px;top:505px">Mild Scoliosis</div>
  <div class="abs caption-blue" style="left:161px;top:505px">Moderate Scoliosis</div>
  <div class="abs caption-blue" style="left:275px;top:505px">Severe Scoliosis</div>
  <div class="abs tiny" style="left:49px;top:521px">10- to 24-degree Cobb<br>Treatment: Monitoring</div>
  <div class="abs tiny" style="left:161px;top:521px">25- to 39-degree Cobb<br>Treatment: <span class="link-red">Bracing</span></div>
  <div class="abs tiny" style="left:275px;top:521px">+40- to 50-degree Cobb<br>Treatment: <span class="link-red">Fusion</span></div>

  <svg class="abs" style="left:0;top:538px" width="401" height="430"><path d="M0 4 C60 -4 110 22 170 24 L401 24 L401 430 L0 430 Z" fill="var(--blue-light)"/></svg>
  <div class="abs h-blue" style="left:37px;top:589px">SOLUTIONS</div>
  <div class="photo brace-photo" style="left:50px;top:625px;width:134px;height:134px" role="img" aria-label="Child wearing a white scoliosis brace"></div>
  <div class="abs h-small-blue" style="left:206px;top:628px">BRACING</div>
  <div class="abs small" style="left:206px;top:653px">For scoliosis patients with Cobb 25-39°<br>Start bracing as early as 2 years old</div>
  <div class="abs small" style="left:206px;top:679px"><span class="bold" style="font-size:8px">Bracing Limitations</span><br>Poor Compliance (50%)<br>Rarely straighten spine<br>Multi-year treatment</div>
  <div class="abs h-small-blue" style="left:47px;top:796px">FUSION</div>
  <div class="photo xray-grey" style="left:212px;top:798px;width:145px;height:90px;border:3px solid #111" role="img" aria-label="Front and side X-rays of a fused spine with rods"></div>
  <div class="abs small" style="left:47px;top:820px;width:160px">For scoliosis patients with Cobb &gt; 40-50°<br>Fusion on early onset scoliosis and adolescent idiopathic scoliosis (AIS) patients</div>
  <div class="abs small" style="left:47px;top:853px;width:160px"><span class="bold" style="font-size:8px">Fusion Limitations</span><br>4+ hour surgery<br>Fusion is irreversible<br>Complications, infections, failures<br>Limiting motion for life<br>Adjacent segment disease: <i>illnesses caused around a fusion site. Most commonly occurs due to physical stress on surrounding spinal segments after a fusion operation</i></div>

  <div class="section" style="top:965px;height:220px;background:var(--blue)">
    <div class="abs h-white" style="left:47px;top:22px;font-size:11px;line-height:1.3">NON-FUSION<br>Vertebral Body Tethering (VBT)</div>
    <div class="photo spine-photo" style="left:47px;top:62px;width:62px;height:135px" role="img" aria-label="Spine model with vertebral body tether"></div>
    <div class="abs small-white" style="left:150px;top:65px;width:205px">Cobb &gt; 40°<br>For early onset scoliosis patients with skeletal growth remaining<br>Ages generally 8-12<br>Procedure currently performed by 15-20 surgeons</div>
    <div class="abs small-white" style="left:150px;top:106px;width:210px"><span class="bold" style="font-size:8px">Limitations</span><br>No ability to adjust tether. Over-correction can result.<br>Tethers break – 10% breakage rate per data submitted to FDA</div>
    <div class="abs small-white ital" style="left:150px;top:141px;width:210px">Halden System recently approved by FDA under HDE Exemption.<br>Provides regulatory clarity</div>
  </div>

  <div class="section" style="top:1185px;height:150px;background:var(--green)">
    <div class="photo" style="left:85px;top:28px;width:260px;height:102px;background:linear-gradient(90deg,rgba(255,255,255,.05),rgba(255,255,255,.18),rgba(255,255,255,.05))" role="img" aria-label="Faint photo of active children behind the icons"></div>
    <div class="abs h-center bold" style="top:17px;font-size:11px">Advantages of VBT over Fusion</div>
    <div class="abs tiny" style="left:84px;top:44px;width:30px;text-align:center;color:#2a3a18">Continued skeletal growth</div>
    <div class="abs tiny" style="left:178px;top:48px;width:40px;text-align:center;color:#2a3a18">Single treatment event</div>
    <div class="abs tiny" style="left:268px;top:44px;width:70px;text-align:center;color:#2a3a18"><b>Does not “burn any bridge”</b><br>Future revision and fusion remain possible</div>
    <div class="icon-dot" style="left:98px;top:81px"></div>
    <div class="icon-dot" style="left:148px;top:81px"></div>
    <div class="icon-dot" style="left:201px;top:81px"></div>
    <div class="icon-dot" style="left:249px;top:81px"></div>
    <div class="icon-dot" style="left:301px;top:81px"></div>
    <div class="abs tiny" style="left:131px;top:102px;width:34px;text-align:center;color:#2a3a18">Partial Motion Preservation</div>
    <div class="abs tiny" style="left:226px;top:102px;width:46px;text-align:center;color:#2a3a18">Little impact on activity and appearance</div>
  </div>

  <div class="abs h-small-blue h-center" style="top:1355px">VBT has Proven Results</div>
  <p class="abs copy" style="left:55px;top:1376px;width:291px;text-align:center;font-size:8.5px">Between the Northbridge group and Dr. Morrow at Bayview University Medical Center (BUMC), 350+ VBT procedures were completed.</p>
  <div class="result-dot" style="left:76px;top:1429px"></div>
  <div class="result-dot" style="left:160px;top:1429px"></div>
  <div class="result-dot" style="left:245px;top:1429px"></div>
  <div class="result-dot" style="left:330px;top:1429px"></div>
  <div class="abs tiny" style="left:41px;top:1455px;width:70px;text-align:center">~66% Cost Savings ($50K compared to $150K)</div>
  <div class="abs tiny" style="left:125px;top:1455px;width:70px;text-align:center">50% Saving in Surgery Time (1.5-2 hrs compared to 4-8 hrs)</div>
  <div class="abs tiny" style="left:210px;top:1455px;width:70px;text-align:center">50% Saving in Hospital Stay (2-3 days compared to 6-7 days)</div>
  <div class="abs tiny" style="left:295px;top:1455px;width:70px;text-align:center">Confirmed improved self-confidence for surgical recipients</div>
</section>

<!-- ============ CONTINUATION COLUMN ============ -->
<section class="col-right">
  <div class="section" style="top:0;height:244px;background:var(--blue)">
    <div class="abs h-white h-center" style="top:20px;font-size:11px">Veltra Dynamic Tethering System – Magnetic Tensioning</div>
    <div class="photo" style="left:192px;top:44px;width:136px;height:140px;background:radial-gradient(ellipse at 50% 50%,#d9c08a 0%,#6b6450 45%,#1d2a33 90%)" role="img" aria-label="Illustration of spine with magnetic tethering implant"></div>
    <div class="photo" style="left:22px;top:45px;width:170px;height:138px;background:rgba(255,255,255,.9)"></div>
    <div class="abs tiny" style="left:70px;top:60px;width:55px">External Magnetic controller</div>
    <div class="abs tiny" style="left:124px;top:53px;width:60px;font-size:4px">Anchoring screw with cleat mechanism</div>
    <div class="abs tiny" style="left:126px;top:88px;font-size:4px">Slider screws</div>
    <div class="abs tiny" style="left:124px;top:130px;width:64px;font-size:4px">Magnetic engine attached to vertebral body via screw. Tether wraps around spool. Spool powered via external controller</div>
    <svg class="abs" style="left:150px;top:55px" width="80" height="100"><g stroke="#7ec242" stroke-width=".8" fill="none"><path d="M30 4L70 20M30 38L70 30M30 38L70 45M30 38L70 60M30 80L70 72M30 80L70 85"/></g></svg>
    <ul class="menu-panel" style="left:0;top:80px;width:110px;height:105px;padding-top:2px">
      <li style="padding-left:34px">Mission</li>
      <li style="padding-left:34px">The Problems</li>
      <li style="padding-left:34px">Solutions</li>
      <li style="padding-left:34px">Vertebral Body Tethering (VBT)</li>
      <li style="padding-left:34px">Advantages of VBT</li>
      <li class="is-active" style="padding-left:34px">Magnetic Tensioning</li>
      <li style="padding-left:34px">Pilot Pig Study</li>
      <li style="padding-left:34px">Tethering Marketing Segments</li>
      <li style="padding-left:34px">Timeline</li>
      <li style="padding-left:34px">Accomplishment</li>
      <li style="padding-left:34px">Key Points for Investment</li>
      <li style="padding-left:34px">Founding Team</li>
    </ul>
    <svg class="abs" style="left:36px;top:70px" width="9" height="9"><path d="M0 0L9 9M9 0L0 9" stroke="var(--green)" stroke-width="1.3"/></svg>
    <p class="abs h-center" style="top:188px;font-size:8px;line-height:1.28;color:#10283a">Magnetically activated dynamic tension<br>Complete non-surgical adjustment<br>Most effective in making gradual non-surgical adjustments over time<br>Prevents over-correction and can act as internal brace</p>
  </div>

  <div class="abs h-small-blue h-center" style="top:264px">Pilot Pig Study</div>
  <p class="abs h-center" style="top:283px;font-size:8px;line-height:1.28;color:var(--body)">2 Pigs – 3months old, 25KG<br>Xrays every 2 weeks.&nbsp;&nbsp; Adjustments made<br>10 weeks total&nbsp; Pigs doubled in size<br>Testing system performance and durability<br>System remained functioning and intact throughout</p>
  <div class="abs h-center bold" style="top:349px;font-size:9px">Pig Study #1 AP View</div>
  <div class="photo xray-grey" style="left:49px;top:369px;width:75px;height:95px" role="img" aria-label="X-ray right after implant surgery"></div>
  <div class="photo xray-grey" style="left:156px;top:369px;width:75px;height:95px;filter:brightness(.7)" role="img" aria-label="X-ray two weeks after surgery"></div>
  <div class="photo xray-grey" style="left:264px;top:369px;width:75px;height:95px" role="img" aria-label="X-ray after tensioning"></div>
  <div class="abs bold" style="left:49px;top:473px;width:75px;text-align:center;font-size:6px">Post Op</div>
  <div class="abs bold" style="left:156px;top:473px;width:75px;text-align:center;font-size:6px">2 Weeks Post Op</div>
  <div class="abs bold" style="left:264px;top:473px;width:75px;text-align:center;font-size:6px">After tensioning</div>

  <div class="section" style="top:500px;height:222px;background:var(--green);border-bottom-left-radius:80% 22px">
    <div class="abs h-white h-center" style="top:19px;font-size:10.5px">Tethering Market Segments</div>
    <div class="card" style="left:34px;top:47px;width:321px;height:139px">
      <div class="market-col" style="left:0">
        <div class="coin" style="left:40px;top:13px">$300M</div>
        <div class="abs" style="left:0;top:50px;width:106px;text-align:center;font-size:5px;color:#7cbb2a">Current Tether Market</div>
        <ul><li>8-12 y/o</li><li>Cobb &gt; 40 degrees</li><li>Growth remaining</li><li>Flexible spine</li><li>10,000 patients</li></ul>
      </div>
      <div class="market-col" style="left:107px">
        <div class="coin" style="left:38px;top:13px">$400M</div>
        <div class="abs" style="left:0;top:50px;width:106px;text-align:center;font-size:5px;color:#7cbb2a">Future Market – AIS Fusion</div>
        <ul><li>10-16 y/o</li><li>Cobb &gt; 40 degrees</li><li>Close to <b>skeletal maturity</b></li><li>Regular “brace-like” adjustments with non-surgical system (magnetic engine)</li><li>30,000 patients</li></ul>
      </div>
      <div class="market-col" style="left:214px">
        <div class="coin" style="left:38px;top:13px">$1B+</div>
        <div class="abs" style="left:0;top:50px;width:106px;text-align:center;font-size:5px;color:#7cbb2a">Future Market – Early Intervention</div>
        <ul><li>Cobb 30-40 degrees</li><li>Never progress to fusion, never wear a brace</li><li>Develop laparoscopic system</li><li>100K+patients</li></ul>
      </div>
      <svg class="abs" style="left:0;top:58px" width="321" height="10"><g fill="#6fa5cf"><path d="M47 2h12l-6 5z"/><path d="M154 2h12l-6 5z"/><path d="M262 2h12l-6 5z"/></g><g stroke="#9cc7e6" stroke-width=".8"><path d="M10 2H47M59 2H154M166 2H262M274 2H312"/></g></svg>
    </div>
  </div>

  <div class="abs h-small-blue h-center" style="top:746px">Timeline to First-In-Man and Financing</div>
  <div class="timeline" style="left:35px">
    <div class="tl-col" style="left:6px"><div class="tl-head">H1 2020</div><div class="tl-tick"></div><ul><li>Complete $2M financing</li><li>Design Freeze</li><li>V&amp;V testing</li><li>Additional in vivo animal trial</li></ul></div>
    <div class="tl-col" style="left:52px"><div class="tl-head">H2 2020</div><div class="tl-tick"></div><ul><li>Identify First-in-man location</li><li>Submit IDE</li></ul></div>
    <div class="tl-col" style="left:97px"><div class="tl-head">H1 2021</div><div class="tl-tick"></div><ul><li>First-in-man trial begins</li><li>$10M financing</li></ul></div>
    <div class="tl-col" style="left:142px"><div class="tl-head">H2 2021</div><div class="tl-tick"></div><ul><li>CE Mark</li><li>Complete enrollment in FIM</li></ul></div>
    <div class="tl-col" style="left:187px"><div class="tl-head">H1 2022</div><div class="tl-tick"></div><ul><li>Commence trial on AIS internal brace patients</li></ul></div>
    <div class="tl-col" style="left:232px"><div class="tl-head">H2 2022</div><div class="tl-tick"></div><ul><li>Continue European cases</li><li>Prepare HDE submission</li></ul></div>
    <div class="tl-col" style="left:276px"><div class="tl-head">H1 2023</div><div class="tl-tick"></div><ul><li>Initial HDE approval – Growth Modulation</li><li>$10M financing</li></ul></div>
  </div>

  <div class="abs h-small-blue" style="left:37px;top:923px;font-size:10px">Accomplishments to Date</div>
  <ul class="abs bullets" style="left:37px;top:940px;width:330px">
    <li>Successful completion of pilot animal trial</li>
    <li>Fully functional system validated in vivo for 10 weeks with no clinical complications</li>
    <li>Positive dialogue with FDA on regulatory strategy, given recent Halden approval</li>
    <li>Winner and grant recipient of the “Pitch Your Pediatric Device!” competition hosted by The Riverside Consortium for Pediatric Device Innovation (2019)</li>
  </ul>

  <svg class="abs" style="left:0;top:1022px" width="386" height="235"><path d="M0 10 C80 0 160 4 386 2 L386 233 L0 233 Z" fill="var(--green)"/></svg>
  <div class="abs h-white h-center" style="top:1062px;font-size:10.5px">Key Points for Investment</div>
  <div class="card" style="left:35px;top:1081px;width:316px;height:144px">
    <div class="abs" style="left:32px;top:21px;width:106px;height:106px;border-radius:50%;border:4px solid #dfe7e8;background:var(--teal)" role="img" aria-label="Investment icon of a hand holding a coin"></div>
    <div class="kp-row" style="top:17px"><span class="kp-icon"></span>Vertebral Body Tethering procedure<br>- potential non-fusion game-changer</div>
    <div class="kp-row" style="top:52px"><span class="kp-icon"></span>Dynamic system is the key</div>
    <div class="kp-row" style="top:78px"><span class="kp-icon"></span>Experienced team with a previous<br>successful exit in the spinal implant<br>market</div>
    <div class="kp-row" style="top:108px"><span class="kp-icon"></span>$20-30M total capital</div>
    <div class="kp-row" style="top:123px">$200-$600M Exit within 5 years</div>
  </div>

  <div class="abs h-small-blue h-center" style="top:1281px">Founding Team – Experience in Orthopedic Implants</div>
  <div class="member" style="left:35px;top:1307px" role="group"><div class="member-photo" role="img" aria-label="Portrait photo"></div><div class="member-name">Peter Lanford</div><div class="team-role">Founder and CEO</div></div>
  <div class="member" style="left:144px;top:1307px"><div class="member-photo" role="img" aria-label="Portrait photo"></div><div class="member-name">Ravi Menon Ph.D.</div><div class="team-role">Co-Founder Chief Science Officer</div></div>
  <div class="member" style="left:252px;top:1307px"><div class="member-photo" role="img" aria-label="Portrait photo"></div><div class="member-name">Mark Ellison</div><div class="team-role">Co-Founder VP R&amp;D and Operations</div></div>
  <div class="member" style="left:35px;top:1340px"><div class="member-photo" role="img" aria-label="Portrait photo"></div><div class="member-name">Evan Tasker</div><div class="team-role">Co-founder and Senior R&amp;D Engineer</div></div>
  <div class="member" style="left:144px;top:1340px"><div class="member-photo" role="img" aria-label="Portrait photo"></div><div class="member-name">Daniel Morrow, MD</div><div class="team-role">Professor and Chief of Pediatric Orthopedics, BUMC</div></div>
  <div class="member" style="left:252px;top:1340px"><div class="member-photo" role="img" aria-label="Portrait photo"></div><div class="member-name">Arjun Patel, MD</div><div class="team-role">Professor of Surgery and Director of Spine Trauma at Lakeside Medical Center</div></div>
  <div class="member" style="left:35px;top:1375px"><div class="member-photo" role="img" aria-label="Portrait photo"></div><div class="member-name">Glen Whitaker, MD</div><div class="team-role">Medical Director of the Desert Spine Group and Clinical Professor at a state school of medicine</div></div>
  <div class="member" style="left:144px;top:1375px"><div class="member-photo" role="img" aria-label="Portrait photo"></div><div class="member-name">Vikram Sethi, MD</div><div class="team-role">Professor of Surgery and Pediatrics at Eastbrook Children’s Hospital</div></div>
  <div class="member" style="left:252px;top:1375px"><div class="member-photo" role="img" aria-label="Portrait photo"></div><div class="member-name">Kevin Park, MD</div><div class="team-role">Neurosurgeon at Northbridge Hospital for Children</div></div>

  <div class="photo" style="left:0;top:1430px;width:386px;height:70px;background:linear-gradient(90deg,#e6ead8,#7d8c55 30%,#c9d2a8 55%,#5d6b3c 80%,#aab68a)" role="img" aria-label="Green-toned photo of a spine model"></div>
</section>

<!-- ============ DESIGN NOTES ============ -->
<div class="note" style="left:258px;top:42px">Show<br>Menu</div>
<div class="note" style="left:498px;top:34px">Hide<br>menu</div>
<div class="note" style="left:632px;top:41px">Fixed menu</div>
<svg class="abs" style="left:0;top:0;pointer-events:none" width="1500" height="700">
  <g fill="none" stroke="var(--red)" stroke-width="1.5">
    <path d="M250 58 C220 56 192 64 184 78"/>
    <path d="M178 70 L184 79 L192 72"/>
    <path d="M544 52 C566 56 582 64 592 76"/>
    <path d="M582 75 L593 77 L590 67"/>
    <path d="M642 62 C660 70 662 86 660 100"/>
    <path d="M654 92 L660 101 L666 92"/>
    <path d="M640 62 L1015 145"/>
    <path d="M912 240 L912 630 C915 650 930 666 978 665 L978 500 C978 420 975 330 1000 290 C1015 270 1025 290 1022 310 L1022 355"/>
    <path d="M1014 345 L1022 357 L1030 345"/>
  </g>
</svg>

</main>
</body>
</html>
```